Online travel site needs edgy website design

tripvane is the first Global Business Travel Website that provides the most comprehensive destination information tailored to suit the business traveller.

It is a ‘one click solution’ that offers direct access to all aspects of business travel, including general information on the city, accommodation and transportation options, economic and financial statistics, key business and services contacts, as well as leisure activities, entertainment suggestions, and listings for any personal needs.

Much more than a travel website, tripvane.com eliminates the need to buy multiple travel books or visit scores of websites. Most importantly, it is the only website that will cover such an extensive range of destinations around the world, while also featuring cities where information is really scarce. The user-friendly and consistent format for all destinations will allow the business traveller to easily navigate through more than 100 information pages on any destination.

tripvane will be simple to navigate, intuitive, unique in design, dynamic, and content rich providing a supreme user experience during navigation of the website.

The website will initially be English and is set to expand to more languages in the future.

A beta site with back-end database has been built - and now we need an edgy state of the art graphic design to reskin it.

LOOK & FEEL

Scope
The design of the site should reflect tripvane’s corporate and user centric philosophy with the following elements:

a. tripvane corporate image and branding
b. the promotion of each city destination
c. tripvane being the starting point of travel, while also a partner during travel
d. the subtle but powerful presence of advertising and sponsorship

All the above must derive from the design outline and elements that are going to be used.

Design Guidelines

Innovative and elegant design, minimalism, simplicity that permits the offering of the required information to be delivered in line with the values of Trust, Care, Discovery & Connection.

In addition:

1. The usability, navigation and the informative character of the corporate web site should not be compromised by the design.
2. The over-segmented pages and over-crowded content per page should be avoided.
3. The design should not only guide the user in an inviting way to the information required but also to intrigue them for further navigation.
4. Advertising space should be anticipated in line with the design character and DMQ standard ad sizes.
5. The use of photos / videos should also encouraged.

Key Elements

a. Branding/Logos
Throughout the website branding should be present as a “guarantee seal” for the content accuracy. Corporate logo should be placed on every page while branding should also characterise any content element and/or tool. Appendix contains the current brand guidelines. Should additional sub-logos be required for specific sections, these should be proposed.

b. Fonts
Provided your experience on the website design you are requested to propose alternative font types and sizes always taken into consideration the inviting and user friendly character that the new website should aspire to. The font type that will be proposed must be user friendly in English typography, but also could support other languages in the future.

Given the fact that the majority of the text in the website contains information and listing, the fonts and text layout should not strain and fatigue the reader.

c. SEO
The design should be friendly towards the search engines.

d. Colours
Colour is considered as an integral part of the brand identity. Tripvane.com corporate colours are orange and grey as per the Attached document reference guide.

Different tonalities of the brand colours, or colours in general, should be proposed and applied, guided always by the above described scope of Look & Feel.

e. Section Headings
As presented above, the site’s section headings (refer Overview of the Site.) The principle is to label the content following users’ needs and mindset. However, the label space should be flexible for changes. The labels should facilitate the user to understand the content they host. This is important and should be applied especially to informative content.

Another function that Headings should perform is that of promoting the website’s content, especially when this kind of content will make the user spend more time in the website. This category of Headings should be approached in a more creative and attractive way as to intrigue users to check the content hosted.

f. Icons
Icons are considered necessary in order to provide the user extra help to guide them to reach the information they need quick n’ easy. Icons not only contribute actively to the creation of an attractive look & feel but, most importantly, facilitate navigation and speed up the users’ familiarisation with the website too.

Therefore their design should be eye-catching, comprehensive and dynamic, in accordance to the new site’s colour coding and following the latest trends as these were defined by the look & feel of smart phones.

PIXELHIVE BRIEF REQUIREMENTS
Based on the above, please provide at least two (2) approaches for the following pages – this includes colour palette in line with logo, layout, fonts.

Initial submissions can just address Deliverable 1 & 2 to fine tune design before proceeding further.

Please refer sample screenshots separately attached from raw beta site for content – available for Deliverables 2 -6.

(REFER example sites we like for their creativity: http://www.brindle-studio.example.co.uk/#Background, http://www.rotaclarafestas.example.com.br/, http://pembrookweb.example.co.uk/ )

Deliverable 1: Landing /Home page
- Access log in –
o Free Account or via Workloop/Chatterbox etc
o Membership Access – Login
- How to use the site
- Allowance for video or animation
- Destination Selection
- Blog & Social media links

Deliverable 2: Destination Landing Page / Template
This is essentially a city guide template to be used for all cities throughout the site.

This page clearly depicts the four information sections
1. General
2. Business
3. Leisure
4. Personal

Also this page should include:
- Business News Feed
- Advertising & Sponsorship Spaces (according to DMQ Standards)
- Destination Time, Weather, FX rates (LIVE feeds)
- Tips

Deliverable 3: Follow the above format but show an Internal Content Page – text only with subheadings

Deliverable 4: Follow the above format but show an Internal Content Page – text and photos

Deliverable 5: Follow the above format but show an Internal Content Page – Listing Sections such as Restaurants (this must also include filter categories)

Deliverable 6: Follow the above format but show an Internal Content Page – Top 10 Experiences – this incorporates address and contact details, photo and sub-text

Deliverable 7: The Membership Landing Page which should include:
1. Intro
2. Advertising & Sponsorship Space
3. The four sections
4. Tips Section
Updates

Hi all - just to reiterate that we are open to different approaches in the design.  We only included the existing screen shots of the beta site to provide you with an idea of the content.  We definitely don't want to see anything similar.....we want it to be edgy yet simple and easy to navigate....we want to create an outstanding user experience!  Cheers Tripvane Team

Reason: Dear Designers - We are extending the period as have not had many submissions at all and want to provide more time. If you have already submitted, we will be in touch shortly with feedback. Thanks for your understanding Tripvane Team

Reason: We would like to give everyone more time so we can find the best and most preferred design.

Target Market(s)

TARGET MARKET
tripvane is a consumer focused website, offering a wide-range of easy-to-use and interactive platforms, for informative and commercial purposes, while also providing attractive and innovative advertising real-estate for potential business partners.

The target audience can be segmented as follows:

Primary Target: Professionals travelling on Business

They require up-to-date reliable information prior and during their travel, as well as facilitation to take action. They need an online Personal Assistant.

The personal characteristics of the primary target group are: busy life, tailored solutions, reliable sources, trusting, caring, and spoiled.
 
The website will have a membership option (for a small annual fee) which will provide customized information for their demographic and preferences. Sub target groups will include:
1. Business Men 40 years
3. Business Women 40 years
5. Business People with reduced mobility

Demographic & Travelling Profile of Business Travellers

• 92% of them use the internet as a source of info
• 54% are males, 38 years old
• 80% holds a college/university degree
• 68% is travelling mainly for leisure and annually 6 times per year
• 52% reserve their ticket through the internet
• 66% is travel internationally

Secondary Targets:

Executive PA’s
Executive personal assistants who need to plan their manager’s travel and provide support information for their trip.

Professionals travelling for Leisure and Partners
They have most probably used the website for their business travel, but consider it also useful for their leisure travel. The generic website, will include enough information to cover most of the leisure needs, as well as the requirements of their partners.

Direct Business-to-Business [B2B] Targets
The direct [B2B] targeted audience includes corporations that would like to use a white label solution for their staff, by using all available destinations or a selected number depending on their global network.

Business-to-Business [B2B] Targets
The [B2B] targeted audience is an indirect audience, for which tripvane promotes its services, and a key revenue stream. The B2B audience consists mainly of a diverse range of professional organisations targeting the business traveller (airlines, hotels, travel agencies, tourism authorities, entertainment companies, services, etc.) tripvane will be targeting these organisations to advertise on the site.
 
Desired Response from Target Groups

The desired response from the consumer targets is:
a) Recurrent use of website
b) Share content/experience with friends and social networking sites
c) Interact on the website’s Blog
d) Register for newsletters and offers
e) Subscribe to Membership
f) Be exposed to commercial advertisements on the website
g) Provide feedback (in the future) for services
h) Use (in the future) online services to purchase products and services
Competition

Industry/Entity Type

Travel

Requirements
Must have
• A clean crisp and professional appearance giving a sense of Trust and Reliability.
Should not have
• It should not look like every other run of the mill travel sites - Roomly.com, Wanderpost etc

```html
<!DOCTYPE html>
<html lang="en">
<head>
<meta charset="utf-8">
<title>tripvane – Professionals Travelling for Leisure and Partners</title>
<link href="https://fonts.googleapis.com/css2?family=PT+Sans:ital,wght@0,400;0,700;1,400&display=swap" rel="stylesheet">
<style>
:root{
  --orange:#f47a20;
  --orange-light:#f9a04a;
  --orange-dark:#e3641a;
  --grey-dark:#3b3b3b;
  --grey:#555;
  --grey-text:#6b6b6b;
  --line:#e6e6e6;
  --panel:#f3f3f3;
  --white:#fff;
}
*{box-sizing:border-box;margin:0;padding:0}
html,body{width:750px;height:1200px;overflow:hidden}
body{position:relative;font-family:"PT Sans",Arial,sans-serif;color:var(--grey);background:var(--white);font-size:8px}
.abs{position:absolute}
.top-backdrop{left:0;top:0;width:750px;height:282px;background:linear-gradient(90deg,#f4f6f7 0%,#eef2f4 55%,#e7e3d3 80%,#d9c69a 100%)}
.top-stripe{left:0;top:0;width:750px;height:3px;background:#555}
.account-bar{left:570px;top:3px;width:119px;height:29px;background:var(--grey-dark);border-radius:0 0 5px 5px;color:#ddd;font-size:8.5px;display:flex;align-items:center;justify-content:space-around;padding:0 8px}
.account-bar span{display:flex;align-items:center;gap:3px}
.logo{left:61px;top:24px;display:flex;align-items:center;gap:8px}
.logo-mark{width:42px;height:42px;background:var(--orange);border-radius:4px}
.logo-name{font-size:36px;font-weight:700;color:var(--orange);letter-spacing:-.5px;line-height:1}
.phone{left:576px;top:38px;font-size:17px;color:var(--grey-dark);display:flex;align-items:center;gap:5px}
.nav{left:61px;top:92px;width:628px;height:33px;background:linear-gradient(#f9913a,#f26f17);display:flex;align-items:center;padding-left:21px;gap:0}
.nav a{color:#fff;text-decoration:none;font-size:11px;margin-right:32px}
.nav .search{position:absolute;right:17px;top:8px;width:161px;height:18px;background:#fff;border-radius:9px;font-size:7px;font-style:italic;color:#aaa;padding:4px 9px}
.nav .search svg{position:absolute;right:7px;top:4px}
.hero{left:61px;top:125px;width:628px;height:215px;background:linear-gradient(180deg,#5a7f9c 0%,#8aa8bf 35%,#c7d3d9 62%,#7b8f8f 80%,#4e6b7a 100%)}
.hero-collage{left:76px;top:190px;width:230px;height:150px;background:linear-gradient(135deg,#d9d2c4,#6aa6c9 45%,#e8a040 75%,#d8d5cc);opacity:.85;transform:skewY(-4deg)}
.hero-title{left:87px;top:142px;color:#fff}
.hero-title .lead{font-size:19px;font-weight:400;line-height:1}
.hero-title .strong{font-size:27px;font-weight:700;line-height:1.1;letter-spacing:.3px}
.hero-dots{left:352px;top:322px;display:flex;gap:4px}
.hero-dots i{width:7px;height:7px;border-radius:50%;background:#eee;display:block}
.tracker{left:473px;top:132px;width:187px;height:199px;background:rgba(245,245,245,.93);border:1px solid #ddd}
.tracker h3{height:28px;background:var(--grey-dark);color:#fff;font-size:14px;font-weight:400;padding:5px 14px}
.tracker .select{margin:8px 0 0 14px;width:158px;height:18px;background:#fff;border:1px solid #ccc;font-size:7.5px;color:#666;padding:3px 7px;position:relative}
.select::after{content:"";position:absolute;right:7px;top:6px;border:3px solid transparent;border-top:4px solid #222}
.tracker .submit{margin:17px auto 0;width:71px;height:19px;background:#2e2e2e;color:#fff;font-size:7.5px;font-weight:700;text-align:center;line-height:19px}
.welcome{left:61px;top:358px;font-size:16px;color:var(--orange)}
.cat-title{font-size:13px;color:var(--grey-dark)}
.cat-photo{width:195px;height:85px}
.cat-text{font-size:7.5px;line-height:15px;color:var(--grey-text);width:200px}
.cat-card{border-right:1px solid #e3e3e3;border-bottom:1px solid #eee}
.finder{left:130px;top:393px;width:348px;height:116px;background:rgba(30,30,30,.9);color:#fff}
.finder label{position:absolute;font-size:10px}
.finder .select{position:absolute;width:136px;height:19px;background:#fff;font-size:7.5px;color:#222;padding:4px 7px}
.finder .go{position:absolute;right:0;bottom:0;width:38px;height:38px;background:var(--orange)}
.blog-tag{left:71px;top:777px;width:47px;height:20px;background:var(--orange);color:#fff;font-size:13px;text-align:center;line-height:20px;border-radius:2px}
.blog-sub{left:125px;top:777px;font-size:13px;color:var(--grey-dark)}
.circle-btn{width:22px;height:22px;border-radius:50%;background:var(--orange);color:#fff;font-size:9px;text-align:center;line-height:22px}
.blog-photo{left:72px;top:810px;width:190px;height:95px;background:linear-gradient(180deg,#9fc6e0 0%,#cfe1ea 30%,#b49a78 45%,#5ac1d6 60%,#2f9fc0 100%)}
.blog-title{left:276px;top:806px;font-size:13px;color:var(--orange)}
.share{left:275px;top:890px;display:flex;gap:4px;font-size:6.5px}
.share span{border:1px solid #ccc;padding:1px 3px;border-radius:2px;background:#f6f6f6;color:#336}
.news-box{left:501px;top:354px;width:188px;height:119px;border:1px solid var(--line)}
.news-box h3{font-size:14px;color:var(--orange);font-weight:400;padding:9px 12px 0;height:31px;border-bottom:1px solid var(--line)}
.news-box p{font-size:7.5px;line-height:15px;color:var(--grey-text);padding:10px 15px 0}
.news-box .date{text-align:right;color:var(--orange);font-size:7.5px;padding:6px 24px 0}
.sidebar-bg{left:501px;top:473px;width:188px;height:296px;background:linear-gradient(90deg,#fff,#f7f7f7)}
.testi-title{left:509px;top:488px;font-size:16px;color:var(--orange)}
.avatar{width:59px;height:59px;border-radius:50%;background:linear-gradient(#c9a58a,#8a6650);border:3px solid #e9e9e9}
.quote{font-size:7.5px;font-style:italic;line-height:15px;color:#555;width:115px}
.byline{font-size:7px;text-align:right;color:#555;line-height:15px}
.subscribe{left:501px;top:769px;width:188px;height:105px;background:#fbf3ea;border:1px solid #f4d2b4}
.subscribe h3{font-size:14px;color:var(--orange);font-weight:400;padding:7px 15px 0}
.subscribe p{font-size:7px;color:var(--grey-text);padding:1px 15px}
.subscribe .email{margin:9px 0 0 15px;width:162px;height:19px;background:#fff;border:1px solid #ddd;font-size:7px;font-style:italic;color:#666;padding:4px 8px}
.subscribe .btn{position:absolute;right:12px;top:73px;width:69px;height:22px;background:#2e2e2e;color:#fff;font-size:8.5px;text-align:center;line-height:22px}
.partners{left:0;top:922px;width:750px;height:73px;border-top:1px solid #eee;display:flex;align-items:center;justify-content:center;gap:29px}
.partners span{font-size:12px;font-weight:700;color:#555;display:flex;align-items:center;gap:5px}
.partners i{display:block;width:10px;height:10px;background:var(--orange)}
.footer{left:0;top:995px;width:750px;height:163px;background:linear-gradient(#f78a2a,#f6a04f 60%,#f58a2b)}
.footer-col{position:absolute;top:26px;color:#fff}
.footer-col h4{font-size:13px;font-weight:400;margin-bottom:8px}
.footer-col p{font-size:7.5px;line-height:14.7px;padding-left:3px}
.footer-col .big{font-size:10px}
.social{display:flex;gap:4px;margin-top:2px}
.social i{display:block;width:20px;height:20px;border-radius:50%;background:#fff}
.bottom{left:0;top:1158px;width:750px;height:38px;background:var(--orange-dark);color:#fff;font-size:7.5px;padding:13px 59px}
.bottom-edge{left:0;top:1196px;width:750px;height:4px;background:#555}
</style>
</head>
<body>
<div class="abs top-backdrop" role="img" aria-label="Soft morning sky fading into golden wheat stalks at the right"></div>
<div class="abs top-stripe"></div>

<div class="abs account-bar">
  <span><svg width="9" height="9" viewBox="0 0 10 10"><circle cx="5" cy="3" r="2.3" fill="#ddd"/><path d="M1 10c0-3 2-4.5 4-4.5S9 7 9 10z" fill="#ddd"/></svg>Register</span>
  <span><svg width="8" height="9" viewBox="0 0 8 10"><path d="M3 0h1.4v5l3 .8L7 10H2.5L0 6.5l1 -.7 2 1.5z" fill="#ddd"/></svg>Login</span>
</div>

<header class="abs logo"><span class="logo-mark"></span><span class="logo-name">tripvane</span></header>
<div class="abs phone"><svg width="13" height="13" viewBox="0 0 14 14"><path d="M3 1l2.2 2.8-1.3 1.4c.8 1.8 2.2 3.2 4 4l1.4-1.3L12 10l-1.2 2.5C6 12 2 8 1.5 3.2z" fill="#777"/></svg>1800.555.019</div>

<nav class="abs nav">
  <a>Categories</a><a>Flights</a><a>Destination</a><a>Blog</a><a>News</a><a>Advertising</a>
  <div class="search">Search here..<svg width="10" height="10" viewBox="0 0 10 10"><circle cx="4" cy="4" r="3" stroke="#888" stroke-width="1.4" fill="none"/><path d="M6.3 6.3L9 9" stroke="#888" stroke-width="1.6"/></svg></div>
</nav>

<section class="abs hero" role="img" aria-label="Cloudy sky over the sea with a hot air balloon"></section>
<div class="abs hero-collage" role="img" aria-label="Scattered travel snapshots, passport and boarding ticket"></div>
<div class="abs hero-title"><div class="lead">Professionals Travelling For</div><div class="strong">LEISURE AND PARTNERS</div></div>
<div class="abs hero-dots"><i></i><i></i><i></i><i></i></div>

<aside class="abs tracker">
  <h3>Flight Tracker</h3>
  <div class="select">Select Airline</div>
  <div class="select">Select Flight</div>
  <div class="select">Depature City</div>
  <div class="select">Arrival City</div>
  <div class="submit">SUBMIT NOW</div>
</aside>

<h2 class="abs welcome" style="font-weight:400">Welcome to Our Website Mainpage</h2>

<!-- General -->
<div class="abs cat-card" style="left:61px;top:387px;width:211px;height:180px"></div>
<div class="abs cat-title" style="left:67px;top:387px">General</div>
<div class="abs cat-photo" role="img" aria-label="Traveller waving beside an aircraft" style="left:66px;top:412px;background:linear-gradient(135deg,#eef2f6,#c9d3dc 50%,#e27a2e 75%,#2d4a78)"></div>
<p class="abs cat-text" style="left:69px;top:499px">Duis tincidunt lectus quis dui viverra vestibulum. Suspendisse vulputate aliquam dui. Nulla elementum dui ut augue. Aliquam vehicula mi at mauris. Maecenas placerat nisl at</p>

<!-- Business -->
<div class="abs cat-card" style="left:276px;top:387px;width:218px;height:180px"></div>
<div class="abs cat-title" style="left:284px;top:387px">Business</div>
<div class="abs cat-photo" role="img" aria-label="Business travellers at an airport" style="left:283px;top:412px;background:linear-gradient(135deg,#6b7d8a,#b9a58c)"></div>
<p class="abs cat-text" style="left:286px;top:499px">Duis tincidunt lectus quis dui viverra vestibulum. Suspendisse vulputate aliquam dui. Nulla elementum dui ut augue. Aliquam vehicula mi at mauris. Maecenas placerat nisl at</p>

<!-- Destination finder -->
<div class="abs finder">
  <label style="left:17px;top:8px">Category</label>
  <div class="select" style="left:18px;top:29px">Travel &amp; Transportation</div>
  <label style="left:17px;top:57px">To</label>
  <div class="select" style="left:18px;top:79px">Select</div>
  <label style="left:170px;top:10px">From</label>
  <div class="select" style="left:168px;top:29px">Select</div>
  <label style="left:170px;top:59px">Currency</label>
  <div class="select" style="left:168px;top:79px">US Dollars</div>
  <div class="go"><svg width="38" height="38" viewBox="0 0 38 38"><circle cx="17" cy="17" r="7" stroke="#fff" stroke-width="2.4" fill="none"/><path d="M22 22l7 7" stroke="#fff" stroke-width="3.4" stroke-linecap="round"/></svg></div>
</div>

<!-- Leisure -->
<div class="abs cat-card" style="left:61px;top:577px;width:211px;height:180px"></div>
<div class="abs cat-title" style="left:67px;top:577px">Leisure</div>
<div class="abs cat-photo" role="img" aria-label="Hikers resting on a rocky coast above a turquoise bay" style="left:66px;top:603px;background:linear-gradient(180deg,#7fb6dc 0%,#2f8fb8 45%,#7a8a6a 70%,#c7b89a 100%)"></div>
<p class="abs cat-text" style="left:69px;top:690px">Duis tincidunt lectus quis dui viverra vestibulum. Suspendisse vulputate aliquam dui. Nulla elementum dui ut augue. Aliquam vehicula mi at mauris. Maecenas placerat nisl at</p>

<!-- Personal -->
<div class="abs cat-card" style="left:276px;top:577px;width:218px;height:180px"></div>
<div class="abs cat-title" style="left:284px;top:577px">Personal</div>
<div class="abs cat-photo" role="img" aria-label="Rolling luggage in an airport terminal" style="left:283px;top:603px;background:linear-gradient(135deg,#c9c9c9,#6e6e6e 55%,#2a2a2a 75%,#b0372c)"></div>
<p class="abs cat-text" style="left:286px;top:690px">Duis tincidunt lectus quis dui viverra vestibulum. Suspendisse vulputate aliquam dui. Nulla elementum dui ut augue. Aliquam vehicula mi at mauris. Maecenas placerat nisl at</p>

<!-- Blog -->
<div class="abs blog-tag">Blog</div>
<div class="abs" style="left:122px;top:778px;width:1px;height:17px;background:#555"></div>
<div class="abs blog-sub" style="left:137px">Travel Tips</div>
<div class="abs circle-btn" style="left:447px;top:773px">‹›</div>
<div class="abs blog-photo" role="img" aria-label="Resort pool with sun loungers and umbrellas"></div>
<h3 class="abs blog-title" style="font-weight:400">Blog Title</h3>
<p class="abs cat-text" style="left:277px;top:826px;width:200px">Duis tincidunt lectus quis dui viverra vestibulum. Suspendisse vulputate aliquam dui. Nulla elementum dui ut augue. Aliquam vehicula mi at mauris. Maecenas placerat nisl at</p>
<div class="abs share"><span>Like</span><span>3k</span><span>Share</span><span>316</span></div>

<!-- Sidebar -->
<aside class="abs news-box">
  <h3>Latest News</h3>
  <p>Duis tincidunt lectus quis dui viverra vestibulum. Suspendisse vulputate aliquam dui. Nulla elementum dui ut augue.</p>
  <div class="date">12-09-2013</div>
</aside>
<div class="abs circle-btn" style="left:651px;top:359px">‹›</div>

<div class="abs sidebar-bg"></div>
<h3 class="abs testi-title" style="font-weight:400">Testimonials</h3>
<div class="abs avatar" role="img" aria-label="Portrait of a smiling client" style="left:506px;top:518px"></div>
<p class="abs quote" style="left:573px;top:527px">Sed ut perspiciatis unde omnis iste natus error sit voluptatem accusantium doloremque l</p>
<div class="abs byline" style="left:510px;top:583px;width:158px">- Daniel Okafor,<br>Project Manger for Brennan and Company</div>
<div class="abs avatar" role="img" aria-label="Portrait of a smiling client" style="left:508px;top:638px"></div>
<p class="abs quote" style="left:575px;top:642px">Sed ut perspiciatis unde omnis iste natus error sit voluptatem accusantium doloremque l</p>
<div class="abs byline" style="left:512px;top:705px;width:158px">- Daniel Okafor,<br>Project Manger for Brennan and Company</div>

<aside class="abs subscribe">
  <h3>Subscribe Newsletters</h3>
  <p>Please subscribe here for latest news.</p>
  <div class="email">email address</div>
  <div class="btn">SUBSCRIBE</div>
</aside>

<!-- Partners -->
<div class="abs partners">
  <span><i></i>Corvale Air</span>
  <span><i></i>Norvik Air</span>
  <span><i></i>Palmetto Air</span>
  <span><i></i>Harbor Jet</span>
  <span><i></i>Crestline</span>
  <span><i></i>Islet Express</span>
</div>

<!-- Footer -->
<footer class="abs footer">
  <div class="footer-col" style="left:63px"><h4>Quick Links</h4><p>Home<br>About Us<br>Categories<br>Flights<br>Destination<br>Blog<br>News</p></div>
  <div class="footer-col" style="left:182px"><h4>Terms and Conditions</h4><p>Privacy Policy<br>Return Policy<br>Terms and Conditions<br>Advertising<br>Contact Us</p></div>
  <div class="footer-col" style="left:351px"><h4>Contact Information</h4><p><span class="big">Tripvane</span><br>48 Larkfield Avenue #4B<br>Easton 20871 ST<br>Phone no. <span class="big">1800.555.287</span><br>Email add: info@tripvane-mail.example</p></div>
  <div class="footer-col" style="left:522px"><h4>Get Connected</h4><div class="social" role="img" aria-label="Social network links"><i></i><i></i><i></i><i></i></div></div>
</footer>
<div class="abs bottom">Copyright © 2013 Company Name.&nbsp; All right reserved.</div>
<div class="abs bottom-edge"></div>
</body>
</html>
```